Wedding dance company needs flyer design

I am looking for a double sided A5 flyer to be designed for my company Step Loft.

The concept of the flyer is to attract couples for their first wedding dance.

This is to support content of our website: http://www.steploftstudio.com/wedding-mix

All the text content for the flyer is attached in flyer.txt. My company logo is attached in logo.zip.

I would like to have 1-2 photos on the flyer based on a couple and their wedding first dance and perhaps some designs without photos (graphics instead).

```html
<!DOCTYPE html>
<html lang="en">
<head>
<meta charset="utf-8">
<title>Step Loft – First Dance Flyer</title>
<link rel="stylesheet" href="https://fonts.googleapis.com/css2?family=Cinzel:wght@400;700&family=Marck+Script&family=Oswald:wght@400;600&family=Lora:ital@0;1&display=swap">
<style>
  :root {
    --pink: #d6367f;
    --pink-dark: #b5236a;
    --pink-light: #ec7fb1;
    --white: #ffffff;
    --ink: #333333;
    --cream: #f4ecd8;
    --gold: #c9a24a;
    --bg: #e9e6e2;
    --photo-top: #8e9474;
    --photo-mid: #c9c4ba;
    --photo-low: #a49d90;
  }
  * { box-sizing: border-box; margin: 0; padding: 0; }
  html, body { width: 1200px; height: 840px; overflow: hidden; background: var(--bg); }
  .canvas { position: relative; width: 1200px; height: 840px; }
  .flyer { position: absolute; top: 52px; width: 520px; height: 735px; overflow: hidden; box-shadow: 0 6px 18px rgba(0,0,0,.18); }
  .flyer--back { left: 40px; background: var(--pink); color: var(--white); }
  .flyer--front { left: 640px; background: var(--white); }

  /* back side */
  .intro { position: absolute; top: 34px; left: 40px; right: 40px; font-family: "Lora", serif; font-size: 13px; line-height: 1.5; }
  .intro p { margin-bottom: 8px; }
  .packages-title { position: absolute; top: 210px; left: 40px; font-family: "Oswald", sans-serif; font-weight: 600; font-size: 24px; letter-spacing: .5px; }
  .packages { position: absolute; top: 258px; left: 40px; right: 40px; display: flex; gap: 14px; }
  .package { flex: 1; height: 118px; background: var(--white); border-top: 16px solid var(--cream); color: var(--ink); padding: 10px 8px; font-family: "Oswald", sans-serif; font-size: 13px; line-height: 1.25; text-align: center; box-shadow: 2px 3px 0 rgba(0,0,0,.15); }
  .package__tier { display: block; background: var(--gold); color: var(--white); font-size: 12px; margin: -20px auto 8px; width: 70px; }
  .offer { position: absolute; top: 396px; left: 40px; right: 40px; font-family: "Oswald", sans-serif; font-size: 15px; font-weight: 600; line-height: 1.35; }
  .swirl-area { position: absolute; top: 450px; left: 0; width: 520px; height: 120px; background: linear-gradient(90deg, rgba(255,255,255,0) 0%, rgba(255,255,255,.18) 50%, rgba(255,255,255,0) 100%); }
  .contact-band { position: absolute; bottom: 0; left: 0; width: 520px; height: 165px; background: var(--white); color: var(--ink); display: flex; align-items: center; padding: 0 30px; gap: 26px; }
  .brand { display: flex; align-items: center; gap: 8px; font-family: "Oswald", sans-serif; font-size: 30px; font-weight: 600; color: var(--pink); white-space: nowrap; }
  .brand__dot { width: 12px; height: 12px; background: var(--pink); border-radius: 50%; }
  .contacts { list-style: none; font-family: "Lora", serif; font-size: 12px; line-height: 1.9; }
  .contacts li { display: flex; align-items: center; gap: 8px; }
  .contacts svg { flex: none; }

  /* front side */
  .photo { position: absolute; inset: 0; background: linear-gradient(180deg, var(--photo-top) 0%, var(--photo-mid) 50%, var(--photo-low) 100%); }
  .front-brand { position: absolute; top: 34px; right: 36px; display: flex; align-items: center; gap: 8px; font-family: "Oswald", sans-serif; font-size: 34px; font-weight: 600; color: var(--white); }
  .front-brand__dot { width: 12px; height: 12px; background: var(--white); border-radius: 50%; }
  .welcome { position: absolute; top: 360px; left: 135px; width: 250px; text-align: center; font-family: "Cinzel", serif; font-weight: 400; font-size: 22px; line-height: 1.05; color: var(--pink); }
  .welcome__rule { display: block; height: 1px; background: var(--ink); margin: 8px 0; }
  .tagline { position: absolute; bottom: 34px; left: 0; width: 470px; height: 128px; background: var(--pink); color: var(--white); display: flex; flex-direction: column; justify-content: center; align-items: center; font-family: "Marck Script", cursive; font-size: 27px; line-height: 1.25; white-space: nowrap; }
</style>
</head>
<body>
<main class="canvas">

  <section class="flyer flyer--back" aria-label="Flyer back">
    <div class="intro">
      <p>Are you feeling nervous about your first dance? Then why not let Step Loft take care of it for you?</p>
      <p>Our friendly teachers will guide you through a routine that suits your song, your style and your budget.</p>
      <p>We work with couples of every level, so no experience is needed to shine on the big day.</p>
    </div>
    <h2 class="packages-title">PACKAGES (STARTING AT £45)</h2>
    <div class="packages">
      <div class="package">Package<br>1 x 1 hr<br>lesson</div>
      <div class="package">Package<br>2 x 1 hr<br>lessons</div>
      <div class="package"><span class="package__tier">Gold</span>Package<br>3 x 1 hr<br>lessons</div>
      <div class="package"><span class="package__tier">Platinum</span>Package<br>4 x 1 hr<br>lessons</div>
    </div>
    <p class="offer">We also offer the SOS last minute package, on-site rehearsals, hen parties and gift vouchers.</p>
    <div class="swirl-area" role="img" aria-label="Decorative white floral swirl ornament"></div>
    <footer class="contact-band">
      <div class="brand"><span class="brand__dot"></span>Step Loft</div>
      <ul class="contacts">
        <li><svg width="14" height="14" viewBox="0 0 14 14"><rect width="14" height="14" rx="3" fill="#d6367f"/><path d="M4 3.5l1.5 0 .7 2-1 .8a5 5 0 0 0 2.5 2.5l.8-1 2 .7v1.5c0 .5-.5 1-1 1A6.5 6.5 0 0 1 3 4.5c0-.5.5-1 1-1z" fill="#fff"/></svg>07700 900123 / 07700 900456</li>
        <li><svg width="14" height="14" viewBox="0 0 14 14"><rect width="14" height="14" rx="3" fill="#d6367f"/><rect x="3" y="4.5" width="8" height="5.5" fill="none" stroke="#fff"/><path d="M3 4.5l4 3 4-3" fill="none" stroke="#fff"/></svg>info@steploftstudio.com</li>
        <li><svg width="14" height="14" viewBox="0 0 14 14"><circle cx="7" cy="7" r="7" fill="#d6367f"/></svg>Twitter: @StepLoftCo</li>
        <li><svg width="14" height="14" viewBox="0 0 14 14"><circle cx="7" cy="7" r="7" fill="#d6367f"/></svg>facebook.com/steploftstudio</li>
        <li><svg width="14" height="14" viewBox="0 0 14 14"><rect width="14" height="14" rx="3" fill="#d6367f"/><circle cx="7" cy="7" r="3.5" fill="none" stroke="#fff"/></svg>www.steploftstudio.com</li>
      </ul>
    </footer>
  </section>

  <section class="flyer flyer--front" aria-label="Flyer front">
    <div class="photo" role="img" aria-label="Photograph of a bride and groom sharing their first dance on a tree-lined cobbled path"></div>
    <div class="front-brand"><span class="front-brand__dot"></span>Step Loft</div>
    <h1 class="welcome">
      <span class="welcome__rule"></span>
      WELCOME<br>TO<br>STEP LOFT
      <span class="welcome__rule"></span>
    </h1>
    <p class="tagline"><span>Make your First Dance</span><span>a performance to be remembered.</span></p>
  </section>

</main>
</body>
</html>
```